Stationery Design Project for Wellmind Therapy Rooms

I would like you to design a letterhead and appt cards and letterhead. i have attached our current brochure so that you can see the kind of clinic that we are - for some context.

Generally our letters will go to General Practitioners.
Appt cards to clients. The text can stay the same as current documents as attached but the design obviously needs to be totally changed.

We are a psychology clinic with several psychologists that work for me. THe psychologists come and go so I am not wanting to list their names on the stationary.

In terms of letterhead my name (dr marnie calloway) needs to be on there..eg dr marnie calloway & associates.

With envelopes we need to be discrete therefore we simply have WTR & our address.

Everything goes under the banner of Wellmind Therapy Rooms Pty Ltd.

I would like it to be consistent in theme/colours with the logo you designed and our website which has just gone live www.wellmindtherapyrooms.com.au

Target Market(s)

General practitioners, potential referrers usually in the medical/health field,

Industry/Entity Type

Clinic

Requirements
Must have
• Logo

Address Suite 4, 287 Kelmore Rd, Brinwood Vale 3172
P 9563 2418 F 9563 2419 E info@wellmindtherapyrooms.com.au
W wellmindtherapyrooms.com.au

Wellmind Therapy Rooms Pty Ltd (small font)
ABN (ill need to provide this) (small font)
Nice to have
• I really like in my website how the colours are graded in the banners...I think this gives a softer feel...so if something like that would look good in our stationary then please use that kind of technique too...but you guys are the experts.

```html
<!DOCTYPE html>
<html lang="en">
<head>
<meta charset="utf-8">
<title>Wellmind Therapy Rooms – Stationery</title>
<link rel="stylesheet" href="https://fonts.googleapis.com/css2?family=Arimo:ital,wght@0,400;0,700;1,400&display=swap">
<style>
  :root {
    --backdrop: #ecebe6;
    --paper: #ffffff;
    --cream: #fbfde8;
    --sage: #d8dbc4;
    --sage-deep: #cdd1b8;
    --ink: #1d1d1d;
    --ink-soft: #444444;
    --brand-grey: #6e6e6e;
    --box-line: #b9b9b4;
    --box-text: #b3b3ae;
    --footer-tint: #f1f2e7;
  }
  * { box-sizing: border-box; margin: 0; padding: 0; }
  html, body { width: 1200px; height: 996px; overflow: hidden; }
  body {
    position: relative;
    background: var(--backdrop);
    font-family: "Arimo", Arial, sans-serif;
    color: var(--ink);
  }
  .sheet { position: absolute; box-shadow: 0 2px 10px rgba(0,0,0,.12); }

  /* shared brand name lockup */
  .brand { position: absolute; display: flex; align-items: center; gap: 8px; }
  .brand-dot { width: 14px; height: 14px; border-radius: 50%; background: var(--brand-grey); flex: none; }
  .brand-name {
    color: var(--brand-grey); font-weight: 400; text-transform: uppercase;
    letter-spacing: .16em; line-height: 1.2;
  }
  .brand-name span { display: block; }

  .rule { position: absolute; height: 5px; background: var(--brand-grey); }

  /* card back */
  .card-back {
    left: 242px; top: 50px; width: 332px; height: 546px;
    background: linear-gradient(170deg, var(--cream) 0%, #f0f2da 45%, var(--sage) 100%);
  }
  .card-back .brand { left: 82px; top: 246px; }
  .card-back .brand-name { font-size: 14px; }

  /* letterhead */
  .letterhead { left: 604px; top: 50px; width: 536px; height: 761px; background: var(--paper); }
  .letterhead .rule-left { left: 0; top: 55px; width: 32px; }
  .letterhead .rule-right { left: 198px; top: 55px; width: 338px; }
  .letterhead .brand { left: 38px; top: 36px; gap: 6px; }
  .letterhead .brand-dot { width: 11px; height: 11px; }
  .letterhead .brand-name { font-size: 9px; }
  .lh-details { position: absolute; top: 67px; font-size: 7px; line-height: 10px; color: var(--ink-soft); }
  .lh-details strong { color: var(--ink); }
  .lh-company { left: 198px; }
  .lh-contact { left: 369px; }

  /* appointment card */
  .appt-card {
    left: 54px; top: 379px; width: 332px; height: 545px;
    background: linear-gradient(180deg, var(--cream) 0%, #f7f8e6 75%, var(--footer-tint) 100%);
  }
  .appt-card .rule-left { left: 0; top: 44px; width: 36px; }
  .appt-card .rule-right { left: 203px; top: 44px; width: 129px; }
  .appt-card .brand { left: 42px; top: 26px; }
  .appt-card .brand-name { font-size: 11px; }
  .field-label { position: absolute; left: 40px; font-size: 11px; font-weight: 700; }
  .psychologist-box {
    position: absolute; left: 148px; top: 90px; width: 148px; height: 25px;
    border: 2px solid var(--box-line); border-radius: 3px; background: var(--paper);
  }
  .slot-row { position: absolute; left: 49px; display: flex; align-items: center; font-size: 10.5px; color: var(--ink-soft); }
  .slot-row .row-label { width: 37px; }
  .slot-box {
    width: 23px; height: 23px; margin-right: 2px;
    border: 2px solid var(--box-line); border-radius: 3px; background: var(--paper);
    font-size: 9px; color: var(--box-text); display: flex; align-items: center; justify-content: center;
  }
  .slot-sep { width: 14px; text-align: center; color: var(--ink); font-weight: 700; }
  .cancel-note { position: absolute; left: 44px; top: 378px; width: 250px; font-size: 10px; font-style: italic; line-height: 16px; color: var(--ink-soft); }
  .appt-card .footer-rule { left: 0; top: 438px; width: 332px; }
  .card-footer {
    position: absolute; left: 0; top: 443px; width: 332px; height: 102px;
    background: var(--footer-tint); padding: 10px 0 0 37px;
    font-size: 10px; line-height: 15px; color: var(--ink-soft);
  }
  .card-footer strong { color: var(--ink); }

  /* envelope */
  .envelope {
    left: 408px; top: 611px; width: 606px; height: 287px;
    background: linear-gradient(100deg, #f8f9e6 0%, #e9ebd6 45%, var(--sage-deep) 100%);
  }
  .recipient { position: absolute; left: 24px; top: 40px; font-size: 10px; line-height: 12px; color: var(--ink-soft); }
  .recipient strong { color: var(--ink); }
  .envelope .brand { left: 443px; top: 118px; }
  .envelope .brand-name { font-size: 16px; letter-spacing: .2em; }
  .return-address {
    position: absolute; left: 443px; top: 146px; width: 150px;
    font-size: 8px; line-height: 11px; color: var(--brand-grey);
  }
</style>
</head>
<body>

  <section class="sheet card-back" aria-label="Appointment card, reverse">
    <div class="brand">
      <div class="brand-dot"></div>
      <div class="brand-name"><span>Wellmind</span><span>Therapy</span><span>Rooms</span></div>
    </div>
  </section>

  <section class="sheet letterhead" aria-label="Letterhead">
    <div class="rule rule-left"></div>
    <div class="rule rule-right"></div>
    <div class="brand">
      <div class="brand-dot"></div>
      <div class="brand-name"><span>Wellmind</span><span>Therapy</span><span>Rooms</span></div>
    </div>
    <div class="lh-details lh-company">
      <strong>Wellmind Therapy Rooms Pty Ltd</strong><br>
      dr marnie calloway &amp; associates<br>
      Suite 4, 287 Kelmore Rd, Brinwood Vale 3172
    </div>
    <div class="lh-details lh-contact">
      <strong>Phone:</strong> 9563 2418 <strong>Fax</strong> 9563 2419<br>
      info@wellmindtherapyrooms.com.au
    </div>
  </section>

  <section class="sheet envelope" aria-label="Envelope">
    <p class="recipient"><strong>Name Surname</strong>, Company<br>City, State, Country, Zip</p>
    <div class="brand">
      <div class="brand-dot"></div>
      <div class="brand-name">WTR</div>
    </div>
    <p class="return-address">Suite 4, 287 Kelmore Rd<br>Brinwood Vale 3172</p>
  </section>

  <section class="sheet appt-card" aria-label="Appointment card, front">
    <div class="rule rule-left"></div>
    <div class="rule rule-right"></div>
    <div class="brand">
      <div class="brand-dot"></div>
      <div class="brand-name"><span>Wellmind</span><span>Therapy</span><span>Rooms</span></div>
    </div>

    <p class="field-label" style="top:96px">Your psychologist:</p>
    <div class="psychologist-box"></div>
    <p class="field-label" style="top:124px">Your appointments:</p>

    <div class="slot-row" style="top:149px"><span class="row-label">Date :</span>
      <span class="slot-box">Y</span><span class="slot-box">Y</span><span class="slot-box">M</span><span class="slot-box">M</span><span class="slot-box">D</span><span class="slot-box">D</span></div>
    <div class="slot-row" style="top:184px"><span class="row-label">Time :</span>
      <span class="slot-box">h</span><span class="slot-box">h</span><span class="slot-sep">:</span><span class="slot-box">m</span><span class="slot-box">m</span></div>

    <div class="slot-row" style="top:227px"><span class="row-label">Date :</span>
      <span class="slot-box">Y</span><span class="slot-box">Y</span><span class="slot-box">M</span><span class="slot-box">M</span><span class="slot-box">D</span><span class="slot-box">D</span></div>
    <div class="slot-row" style="top:260px"><span class="row-label">Time :</span>
      <span class="slot-box">h</span><span class="slot-box">h</span><span class="slot-sep">:</span><span class="slot-box">m</span><span class="slot-box">m</span></div>

    <div class="slot-row" style="top:299px"><span class="row-label">Date :</span>
      <span class="slot-box">Y</span><span class="slot-box">Y</span><span class="slot-box">M</span><span class="slot-box">M</span><span class="slot-box">D</span><span class="slot-box">D</span></div>
    <div class="slot-row" style="top:332px"><span class="row-label">Time :</span>
      <span class="slot-box">h</span><span class="slot-box">h</span><span class="slot-sep">:</span><span class="slot-box">m</span><span class="slot-box">m</span></div>

    <p class="cancel-note">Please note fees will be charged for missing appointments without 48 hour notice</p>

    <div class="rule footer-rule"></div>
    <div class="card-footer">
      <strong>Wellmind Therapy Rooms Pty Ltd</strong><br>
      Suite 4, 287 Kelmore Rd, Brinwood Vale 3172<br>
      <strong>Phone:</strong> 9563 2418 <strong>Fax</strong> 9563 2419<br>
      info@wellmindtherapyrooms.com.au
    </div>
  </section>

</body>
</html>
```